A4 Flyer Design outlining our financial philosophy

One A4 page design (landscape orientation) outlining our financial philosophy.
The design needs to show these steps as the building blocks and the path taken to financial success:
1. Maximise income and reduce expenses
2. Maximise savings and reduce bad debts
3. Invest wisely & tax effectively
4. Manage risk
5. Plan for retirement
6. Leave a legacy
The design needs to incorporate the 6 building blocks above along with the key points for each topic. More info attached.
Design must be engaging, professional and consistent with our current branding colours.

Target Market(s)

self employed individuals looking to build wealth through property and shares.

Industry/Entity Type

Financial Planning

Font styles to use
Sans Serif

Colors
0255a3
5c5c5c
000000
ffffff

Requirements
Must have
• clear and engaging.
• consistent with current branding
• 6 topics with key considerations (as per attached)
• must show that all 6 points are linked and are a journey.

```html
<!DOCTYPE html>
<html lang="en">
<head>
<meta charset="utf-8">
<title>Meridian Financial Group – Our financial philosophy</title>
<link rel="stylesheet" href="https://fonts.googleapis.com/css2?family=Roboto:wght@700&family=Oswald:wght@400;500&family=Open+Sans:wght@600&display=swap">
<style>
  :root{
    --brand-blue:#0255a3;
    --bright-blue:#1a5ee8;
    --deep-blue:#0a3fd0;
    --sky-blue:#1aa3f0;
    --grey:#5c5c5c;
    --white:#ffffff;
    --black:#000000;
  }
  *{box-sizing:border-box;margin:0;padding:0}
  html,body{width:1200px;height:848px;overflow:hidden;background:var(--white)}
  .flyer{
    position:relative;width:1200px;height:848px;overflow:hidden;
    background:
      radial-gradient(ellipse 700px 500px at 380px 420px, rgba(20,60,190,.55), transparent 70%),
      linear-gradient(160deg,var(--sky-blue) 0%,var(--bright-blue) 35%,var(--deep-blue) 100%);
    font-family:"Open Sans",sans-serif;color:var(--white);
  }
  .hero-figure{
    position:absolute;left:940px;top:280px;width:260px;height:460px;
    background:radial-gradient(ellipse at 50% 40%,rgba(70,130,230,.55),rgba(20,70,220,0) 70%);
  }
  .brand{
    position:absolute;left:66px;top:23px;width:279px;height:88px;background:var(--white);
    display:flex;align-items:center;gap:12px;padding-left:18px;
  }
  .brand-mark{width:52px;height:52px;border-radius:50%;background:var(--brand-blue);flex:none}
  .brand-name{font-family:"Roboto",sans-serif;font-weight:700;color:var(--brand-blue);font-size:19px;line-height:1.15}
  .title{
    position:absolute;left:393px;top:30px;font-family:"Roboto",sans-serif;font-weight:700;
    font-size:58px;letter-spacing:-.5px;white-space:nowrap;
  }
  .connectors{position:absolute;left:0;top:0}
  .step{
    position:absolute;width:162px;height:162px;border-radius:50%;background:var(--white);
    display:flex;flex-direction:column;align-items:center;justify-content:center;text-align:center;
  }
  .step-number{
    width:32px;height:32px;background:var(--bright-blue);transform:rotate(45deg);
    display:flex;align-items:center;justify-content:center;margin-bottom:14px;margin-top:-6px;
  }
  .step-number span{transform:rotate(-45deg);font-family:"Oswald",sans-serif;font-weight:500;font-size:20px;color:var(--white)}
  .step-title{font-family:"Oswald",sans-serif;font-weight:400;font-size:17.5px;line-height:1.2;color:var(--brand-blue)}
  .checklist{position:absolute;list-style:none;font-size:10px;line-height:1.2}
  .checklist li{position:relative;padding-left:19px;margin-bottom:7px}
  .checklist li::before{content:"";position:absolute;left:0;top:1px;width:9px;height:9px;background:var(--white);border-radius:1px}
  .checklist li::after{content:"";position:absolute;left:3px;top:2.5px;width:2.5px;height:4.5px;border:solid var(--brand-blue);border-width:0 1.5px 1.5px 0;transform:rotate(45deg)}
  .result-line{position:absolute;left:912px;top:192px;width:3px;height:579px;background:var(--white)}
  .result-badge{
    position:absolute;left:1030px;top:432px;width:68px;height:68px;background:var(--white);transform:rotate(45deg);
  }
  .result-label{
    position:absolute;left:1014px;top:448px;width:100px;text-align:center;
    font-family:"Oswald",sans-serif;font-weight:500;font-size:16px;line-height:1;color:var(--brand-blue);
  }
  .result-text{
    position:absolute;left:954px;top:524px;width:220px;text-align:center;
    font-family:"Oswald",sans-serif;font-weight:500;font-size:26px;
  }
</style>
</head>
<body>
<main class="flyer">
  <div class="hero-figure" role="img" aria-label="Illustration of a celebrating businessman standing on a rising arrow"></div>

  <header class="brand">
    <span class="brand-mark"></span>
    <span class="brand-name">MERIDIAN<br>FINANCIAL GROUP</span>
  </header>
  <h1 class="title">Our financial philosophy</h1>

  <svg class="connectors" width="1200" height="848" viewBox="0 0 1200 848" fill="none" stroke="#fff" stroke-width="2" stroke-dasharray="3 4" aria-hidden="true">
    <path d="M96 340 Q140 360 184 340"/><path d="M140 354 V384"/>
    <path d="M96 566 Q140 586 184 566"/><path d="M140 580 V608"/>
    <path d="M168 798 Q225 780 230 738"/>
    <path d="M222 772 Q250 805 330 803 L430 803 Q492 800 496 736"/>
    <path d="M496 740 Q505 790 566 800"/>
    <path d="M540 624 Q584 604 628 624"/><path d="M584 610 V582"/>
    <path d="M540 398 Q584 378 628 398"/><path d="M584 384 V356"/>
    <g stroke="none" fill="#fff">
      <path d="M135 386 L145 386 L140 394 Z"/>
      <path d="M135 610 L145 610 L140 618 Z"/>
      <path d="M579 580 L589 580 L584 572 Z"/>
      <path d="M579 354 L589 354 L584 346 Z"/>
      <path d="M915 478 H945 V471 L962 481 L945 491 V484 H915 Z"/>
    </g>
  </svg>

  <section class="step" style="left:59px;top:176px">
    <div class="step-number"><span>1</span></div>
    <h2 class="step-title">Maximise Income<br>&amp; Reduce<br>Expenses</h2>
  </section>
  <ul class="checklist" style="left:240px;top:218px">
    <li>Invest in yourself through education and training</li>
    <li>Align your spending with your values</li>
    <li>Build a number of income streams</li>
    <li>Increase surplus income</li>
    <li>Track your spending</li>
  </ul>

  <section class="step" style="left:59px;top:402px">
    <div class="step-number"><span>2</span></div>
    <h2 class="step-title">Maximise Savings /<br>Wquity &amp; Reduce<br>Bad Debts</h2>
  </section>
  <ul class="checklist" style="left:244px;top:447px;width:230px">
    <li>Surplus income in creases savings</li>
    <li>Use savings and equity for investment</li>
    <li>Avoid borrowing for lifestyle assets / experiences where possible</li>
  </ul>

  <section class="step" style="left:59px;top:626px">
    <div class="step-number"><span>3</span></div>
    <h2 class="step-title">Invest Wisely<br>&amp; Effectively</h2>
  </section>
  <ul class="checklist" style="left:247px;top:670px;width:248px">
    <li>Build an investment portfolio e.g. property and shares</li>
    <li>Use appropriate tax structures such as Family Trusts / Superannuation</li>
    <li>Depreciation schedules</li>
  </ul>

  <section class="step" style="left:503px;top:626px">
    <div class="step-number"><span>4</span></div>
    <h2 class="step-title">Manage Risk</h2>
  </section>
  <ul class="checklist" style="left:690px;top:666px">
    <li style="margin-bottom:10px">Insurance in various forms</li>
    <li style="margin-bottom:10px">Contingency plans</li>
    <li style="margin-bottom:10px">Diversification</li>
    <li>Focus on quality</li>
  </ul>

  <section class="step" style="left:503px;top:402px">
    <div class="step-number"><span>5</span></div>
    <h2 class="step-title">Plan For Retirement</h2>
  </section>
  <ul class="checklist" style="left:685px;top:459px;width:216px">
    <li style="margin-bottom:10px">Replacement of your salary or profits from running a business with income from your investment portfolio nest egg</li>
    <li>Drawing a sustainable income to maintain a great lifestyle and protect your retirement nest egg</li>
  </ul>

  <section class="step" style="left:504px;top:174px">
    <div class="step-number"><span>6</span></div>
    <h2 class="step-title">Leave Legacy</h2>
  </section>
  <ul class="checklist" style="left:692px;top:233px">
    <li>Having a Will</li>
    <li>Power of Attorney</li>
    <li>Testamentary Trust?</li>
  </ul>

  <div class="result-line"></div>
  <div class="result-badge"></div>
  <div class="result-label">The<br>Result</div>
  <p class="result-text">Financial Success</p>
</main>
</body>
</html>
```